Sales Flyer for Outdoor Kitchens

Looks to have a trifold flyer designed based off website content / projects. Use www.brickleafyardworks.com for content

```html
<!DOCTYPE html>
<html lang="en">
<head>
<meta charset="utf-8">
<title>Brickleaf Yardworks – Trifold Brochure</title>
<link href="https://fonts.googleapis.com/css2?family=Montserrat:wght@400;500;600;700;800&family=Oswald:wght@600&family=Lora:ital@1&display=swap" rel="stylesheet">
<style>
:root{
  --blue:#1a6fc4;
  --blue-dark:#0b4c9c;
  --blue-deep:#0a3f86;
  --green:#3cb54a;
  --ink:#2a2a2a;
  --muted:#444;
  --paper:#ffffff;
  --stage:#dcdcdc;
  --svc-text:#cfe6ff;
}
*{box-sizing:border-box;margin:0;padding:0}
html,body{width:881px;height:1200px;overflow:hidden}
body{background:var(--stage);font-family:"Montserrat",sans-serif;color:var(--ink);position:relative}
.sheet{position:absolute;left:30px;width:820px;height:579px;background:var(--paper);overflow:hidden}
.sheet--outside{top:14px}
.sheet--inside{top:607px}
.abs{position:absolute}
.photo{position:absolute}
.accent-bar{position:absolute;background:var(--green)}

/* outside – left panel */
.about-title,.clients-title{position:absolute;left:26px;color:var(--blue);font-weight:700;font-size:15px}
.about-title{top:275px}
.clients-title{top:394px}
.about-text{position:absolute;left:26px;top:300px;width:224px;font-size:7.6px;line-height:11.6px;text-align:justify;color:var(--muted)}
.quote{position:absolute;left:43px;font-family:"Lora",serif;font-style:italic;font-size:6.9px;line-height:10.7px;color:var(--muted)}
.quote--one{top:423px;width:210px}
.quote--two{top:516px;width:190px}
.reviewer{position:absolute;font-family:"Lora",serif;font-style:italic;font-size:9px;color:var(--ink)}
.reviewer .stars{color:#f2b61c;font-style:normal;font-size:6.5px;letter-spacing:0.5px;margin-right:5px}

/* outside – middle panel */
.cover-band{position:absolute;left:273.5px;top:0;width:315.5px;height:579px;background:linear-gradient(180deg,#1b6ecb 0%,#1762ba 55%,#0d4c9e 100%)}
.headline{position:absolute;left:352px;top:50px;width:200px;font-family:"Oswald",sans-serif;font-weight:600;font-size:29px;line-height:35px;color:#fff;letter-spacing:0.5px}
.brand-mark{position:absolute;font-weight:700;color:#fff;text-align:center;letter-spacing:0.5px}
.brand-mark--cover{left:320px;top:310px;width:176px;font-size:17px;line-height:20px}
.contact-title{position:absolute;left:320px;top:424px;width:176px;text-align:center;color:var(--green);font-weight:700;font-size:15px}
.contact-list{position:absolute;left:300px;top:458px;width:216px;color:#fff;font-size:7.8px;line-height:10px;list-style:none}
.contact-list li{display:flex;align-items:flex-start;justify-content:center;gap:4px;margin-bottom:5px}
.contact-list li.phone{font-size:11px;font-weight:700;line-height:12px}
.contact-list svg{flex:none;margin-top:1px}

/* outside – right panel */
.brand-mark--front{left:611px;top:34px;width:150px;font-size:12px;line-height:14px;color:var(--green);text-align:left}
.front-title{position:absolute;left:611px;top:104px;line-height:1}
.front-title .soft{display:block;color:var(--blue);font-weight:700;font-size:24px;margin-bottom:3px}
.front-title .strong{display:block;color:var(--green);font-weight:800;font-size:29px;line-height:29px}
.front-title .soft.end{margin-top:4px;margin-bottom:0}
.front-url{position:absolute;right:27px;top:546px;font-size:10px;color:var(--blue);font-weight:500}
.front-url b{color:var(--green);font-weight:700}

/* inside – services */
.services-band{position:absolute;left:0;top:0;width:273.6px;height:579px;background:linear-gradient(180deg,#1b72c6 0%,#1662b7 60%,#0e4f9f 100%)}
.services-title{position:absolute;left:25px;top:22px;color:#fff;font-weight:700;font-size:25px;line-height:25px}
.service{position:absolute;left:26px;width:240px;height:86px}
.service .thumb{position:absolute;left:0;top:0;width:86px;height:86px;border-radius:12px;border:2.5px solid #fff}
.service h3{position:absolute;left:102px;top:8px;width:138px;color:#fff;font-size:12.5px;line-height:15px;font-weight:600}
.service p{position:absolute;left:102px;width:132px;color:var(--svc-text);font-size:8.3px;line-height:11.6px}

/* inside – process */
.process-title{position:absolute;left:303px;top:243px;color:var(--blue);font-weight:800;font-size:19px;line-height:20.5px}
.step{position:absolute;width:200px}
.step h4{font-size:9.4px;font-weight:700;color:var(--ink);margin-bottom:5px}
.step p{font-size:7.1px;line-height:10.2px;text-align:justify;color:var(--muted)}
.step--mid{left:317px}
.step--right{left:587px;width:208px}
.inset-photo{position:absolute;left:640px;top:175px;width:156px;height:115px;border:3px solid #fff}
</style>
</head>
<body>

<!-- OUTSIDE SPREAD -->
<section class="sheet sheet--outside">
  <div class="cover-band" role="img" aria-label="Blue-tinted backyard deck at dusk behind the cover text"></div>

  <div class="photo" style="left:26px;top:30px;width:311px;height:224px;background:linear-gradient(160deg,#8fb6d8 0%,#b9b2a6 35%,#9a8f82 65%,#5b5650 100%)" role="img" aria-label="Stone-clad outdoor kitchen with built-in grill and stainless drawers"></div>
  <div class="accent-bar" style="left:26px;top:254px;width:47px;height:8px"></div>

  <h2 class="about-title">About us</h2>
  <p class="about-text">With over a decade of experience in the industry, Owen Castellan, the owner and operator of Brickleaf, has become a well-known name in the Houston area. His passion for outdoor living spaces, coupled with his keen eye for design and attention to detail, has led him to create some of the most stunning and functional outdoor spaces for his clients.</p>

  <h2 class="clients-title">What our clients say</h2>

  <svg class="abs" style="left:0;top:0" width="300" height="579" aria-hidden="true">
    <path d="M31 438 V488 Q31 493 36 493 H168" fill="none" stroke="var(--green)" stroke-width="1"/>
    <circle cx="31" cy="431" r="6" fill="var(--green)"/>
    <text x="31" y="434.5" fill="#fff" font-size="9" font-weight="700" text-anchor="middle" font-family="Montserrat,sans-serif">“</text>
    <path d="M31 531 V551 Q31 556 36 556 H156" fill="none" stroke="var(--green)" stroke-width="1"/>
    <circle cx="31" cy="524" r="6" fill="var(--green)"/>
    <text x="31" y="527.5" fill="#fff" font-size="9" font-weight="700" text-anchor="middle" font-family="Montserrat,sans-serif">“</text>
  </svg>

  <p class="quote quote--one">We recently had the pleasure of working with Brickleaf Yardworks, LLC to design and construct our dream outdoor kitchen with a grill, burners, outdoor refrigerator and sink and we couldn't be happier with the results. From the initial consultation to the final installation, every step of the process exceeded our expectations.</p>
  <p class="reviewer" style="left:171px;top:487px"><span class="stars">★★★★★</span>Priya T</p>

  <p class="quote quote--two">Owen is exceptional to work; his attention to detail, time management, and quality are outstanding. I highly recommend him.</p>
  <p class="reviewer" style="left:159px;top:550px"><span class="stars">★★★★★</span>Morgan L</p>

  <h1 class="headline">ACHIEVE YOUR DREAM YARD WITH OUR EXPERT GUIDANCE</h1>

  <p class="brand-mark brand-mark--cover">BRICKLEAF<br>YARDWORKS</p>

  <h2 class="contact-title">CONTACT US</h2>
  <ul class="contact-list">
    <li>
      <svg width="8" height="9" viewBox="0 0 8 10"><path d="M4 0a3.5 3.5 0 0 0-3.5 3.5C.5 6 4 10 4 10s3.5-4 3.5-6.5A3.5 3.5 0 0 0 4 0z" fill="var(--green)"/><circle cx="4" cy="3.5" r="1.3" fill="#fff"/></svg>
      <span style="text-align:center">4820 Lantern Creek Rd Ste 210<br>Fairhaven, 77450, US</span>
    </li>
    <li class="phone">
      <svg width="9" height="9" viewBox="0 0 10 10"><circle cx="5" cy="5" r="5" fill="var(--green)"/><path d="M3.2 2.6c.3-.2.6 0 .7.3l.3.7c.1.2 0 .4-.1.5l-.3.3c.3.6.8 1.1 1.4 1.4l.3-.3c.1-.1.3-.2.5-.1l.7.3c.3.1.5.4.3.7-.3.6-.9.9-1.6.6C4.3 6.5 3.5 5.7 3 4.6c-.3-.7 0-1.5.2-2z" fill="#fff"/></svg>
      <span>555-014-2290</span>
    </li>
    <li>
      <svg width="8" height="8" viewBox="0 0 10 10"><circle cx="5" cy="5" r="5" fill="var(--green)"/><rect x="2.5" y="3.3" width="5" height="3.4" fill="#fff"/><path d="M2.5 3.3 5 5.2 7.5 3.3" fill="none" stroke="var(--green)" stroke-width=".6"/></svg>
      <span>oc@brickleafyardworks.com</span>
    </li>
    <li>
      <svg width="8" height="8" viewBox="0 0 10 10"><circle cx="5" cy="5" r="5" fill="var(--green)"/><circle cx="5" cy="5" r="2.7" fill="none" stroke="#fff" stroke-width=".6"/><path d="M2.3 5h5.4M5 2.3c-1.2 1.6-1.2 3.8 0 5.4M5 2.3c1.2 1.6 1.2 3.8 0 5.4" fill="none" stroke="#fff" stroke-width=".5"/></svg>
      <span>www.brickleafyardworks.com</span>
    </li>
  </ul>

  <div class="accent-bar" style="left:580px;top:104px;width:9px;height:107px"></div>
  <div class="abs" style="left:589px;top:0;width:231px;height:579px;background:var(--paper)"></div>
  <div class="accent-bar" style="left:580px;top:104px;width:9px;height:107px"></div>

  <p class="brand-mark brand-mark--front">BRICKLEAF YARDWORKS</p>

  <h1 class="front-title">
    <span class="soft">Create Your</span>
    <span class="strong">DREAM</span>
    <span class="strong">BACKYARD</span>
    <span class="soft end">With Us</span>
  </h1>

  <div class="photo" style="left:545px;top:233px;width:246px;height:295px;background:linear-gradient(170deg,#6fa64a 0%,#9a6a3c 35%,#b87a45 55%,#a64b36 72%,#c9c7c0 85%,#6c9a3e 100%)" role="img" aria-label="Cedar pavilion with gabled roof and brick base on a green lawn"></div>

  <p class="front-url">www.<b>brickleafyardworks</b>.com</p>
</section>

<!-- INSIDE SPREAD -->
<section class="sheet sheet--inside">
  <div class="services-band"></div>
  <div class="accent-bar" style="left:0;top:27px;width:9px;height:44px"></div>
  <h2 class="services-title">Our turnkey<br>services</h2>

  <article class="service" style="top:90px">
    <div class="thumb" style="background:linear-gradient(160deg,#6f9a58,#9c9a96 45%,#a2503c 85%)" role="img" aria-label="Brick outdoor kitchen with stainless grill"></div>
    <h3>OUTDOOR<br>KITCHENS</h3>
    <p style="top:40px">Culinary Excellence in Your Outdoor Sanctuary Welcome to Outdoor Sanctuary</p>
  </article>
  <article class="service" style="top:185px">
    <div class="thumb" style="background:linear-gradient(160deg,#b5773f,#e4e1dc 45%,#a35b32 80%)" role="img" aria-label="Covered patio with wood ceiling and outdoor seating"></div>
    <h3>PAVILIONS, PATIOS<br>&amp; PERGOLAS</h3>
    <p style="top:40px">Pergolas and Patio Covers – Shaping Serenity in Your Backyard</p>
  </article>
  <article class="service" style="top:280px">
    <div class="thumb" style="background:radial-gradient(circle at 50% 55%,#ffb347 0%,#c86a3e 25%,#a8785a 60%,#8c6a4e 100%)" role="img" aria-label="Round stone fire pit with flames"></div>
    <h3 style="top:20px">FIRE PITS</h3>
    <p style="top:38px">Elevate Your Outdoor Space with Unique Fire Features</p>
  </article>
  <article class="service" style="top:374px">
    <div class="thumb" style="background:linear-gradient(180deg,#9cc4e6 0%,#e8e8e6 40%,#5fc6e0 70%,#2aa3cf 100%)" role="img" aria-label="Backyard swimming pool beside a white house"></div>
    <h3 style="top:14px">POOLS</h3>
    <p style="top:32px">Our expert team will create a customized plan that brings together your</p>
  </article>
  <article class="service" style="top:469px">
    <div class="thumb" style="background:radial-gradient(circle at 50% 50%,#d5e86a 0%,#5f9a2c 40%,#274d1a 100%)" role="img" aria-label="Lit garden beds with landscape lighting at night"></div>
    <h3 style="top:2px">LANDSCAPING<br>&amp; LIGHTING</h3>
    <p style="top:33px">Design a captivating backyard oasis with our landscaping service, harmonizing</p>
  </article>

  <div class="photo" style="left:273.6px;top:0;width:272.2px;height:219px;background:linear-gradient(180deg,#4f7a3a 0%,#7c8f5c 30%,#b58a62 60%,#a2714c 100%)" role="img" aria-label="Gravel fire pit area ringed by Adirondack chairs"></div>
  <div class="accent-bar" style="left:303.6px;top:219px;width:47px;height:8px"></div>

  <div class="photo" style="left:545.8px;top:0;width:274.2px;height:219px;background:linear-gradient(170deg,#b57a45 0%,#e6e3de 30%,#c77638 55%,#cfcfcf 80%,#9a9a9a 100%)" role="img" aria-label="Covered patio with chandelier, wood dining set and outdoor kitchen"></div>
  <div class="inset-photo" style="background:linear-gradient(170deg,#6b9a44 0%,#a36a3a 40%,#b5763f 60%,#7f8a5a 100%)" role="img" aria-label="Cedar pavilion with seating beneath, surrounded by trees"></div>

  <h2 class="process-title">EFFECTIVE<br>PROCESSFOR<br>GREAT OUTCOMES</h2>

  <svg class="abs" style="left:0;top:0" width="820" height="579" aria-hidden="true">
    <path d="M305 334 V543 Q305 553 315 553 H518 Q528 553 528 543 V289 Q528 279 538 279 H566 Q576 279 576 289 V486" fill="none" stroke="var(--green)" stroke-width="1.2"/>
    <circle cx="305" cy="333" r="2.6" fill="var(--green)"/>
    <circle cx="305" cy="398" r="2.6" fill="var(--green)"/>
    <circle cx="305" cy="469" r="2.6" fill="var(--green)"/>
    <circle cx="576" cy="302" r="2.6" fill="var(--green)"/>
    <circle cx="576" cy="384" r="2.6" fill="var(--green)"/>
    <circle cx="576" cy="486" r="2.6" fill="var(--green)"/>
  </svg>

  <div class="step step--mid" style="top:328px">
    <h4>TELL US ABOUT YOUR PROJECT</h4>
    <p>This is where you can share your ideas of your dream backyard with us. The more detail you provide the better prepared we can be for the next step but in just a few minutes you can be on your way to a new dream backyard!</p>
  </div>
  <div class="step step--mid" style="top:393px">
    <h4>PHONE CONSULTATION</h4>
    <p>Upon review of your project information plan, we will give you a call to discuss your plans, budgets &amp; timelines. If you choose to proceed, then we will discuss timing of step 3.</p>
  </div>
  <div class="step step--mid" style="top:464px">
    <h4>IN-PERSON CONSULTATION</h4>
    <p>We will visit you at your location and walk through your space to better understand your visions. This is a good time for an initial assessment of project challenges and options to be considered in the next step.</p>
  </div>

  <div class="step step--right" style="top:297px">
    <h4>DESIGN</h4>
    <p>The majority of HOA &amp; municipalities in our area require at least a conceptual plan and construction drawings. We offer an independently contracted design phase for this portion of a project. Design contracts range from $1,500 to $5,000 depending on HOA requirements.</p>
  </div>
  <div class="step step--right" style="top:379px">
    <h4>CONSTRUCTION</h4>
    <p>After HOA &amp; permit approvals we can begin construction. A pre-construction kick off meeting will take place on-site to ensure expectations are aligned. We will communicate with you throughout the entire process to ensure you know who and what to expect at your residence at all times. Typical build times are two to six months, depending on complexity.</p>
  </div>
  <div class="step step--right" style="top:481px">
    <h4>POST CONSTRUCTION WALKTHROUGH</h4>
    <p>Upon completion of your project, the owner of Brickleaf will perform a job site walk with you to ensure everything was completed per the job specifications. We will also discuss maintenance recommendations at this time. Our goal is to leave this walkthrough with your outdoor living space ready to entertain guest the very next day.</p>
  </div>
</section>

</body>
</html>
```